Business Card Design

I need a business card for my rental business. The business is named:
Hire a Vorlatrike Brenmoor
www.hireavorlatrikebrenmoor.example
(555) 014-2937
This will be a business card that I will leave at other businesses as advertisement so it needs to have the name, website, and phone number.
Please feel free to be creative. This is a new business so I have no designs.
Thank you very much for your time and I look forward to receiving your designs
Target Market(s)
Local rental customers
Industry/Entity Type
Business
Contact Information for Business Card
Please check out my website:
Other font styles liked:
- anything creative
Colors
Designer to choose colors to be used in the design.
Requirements
Must have
- Business name, phone, website. Rentals available hourly or daily. Book online

```html
<!DOCTYPE html>
<html lang="fr">
<head>
<meta charset="utf-8">
<title>Hire a Vorlatrike Brenmoor – Business Card</title>
<link rel="stylesheet" href="https://fonts.googleapis.com/css2?family=Antonio:wght@700&family=Jost:wght@600;700&family=Open+Sans:wght@400&display=swap">
<style>
  :root {
    --backdrop: #9a9a95;
    --charcoal: #414042;
    --graphite: #545454;
    --teal-deep: #19a5b1;
    --teal-soft: #6bc9cb;
    --teal-mist: #75c2c3;
    --teal-steel: #35a6ad;
    --paper: #ffffff;
    --paper-grey: #eaeae8;
    --ink-teal: #1a9fab;
  }
  * { margin: 0; padding: 0; box-sizing: border-box; }
  html, body {
    width: 1080px; height: 1200px; overflow: hidden;
    background: var(--backdrop);
  }
  .canvas { position: relative; width: 1080px; height: 1200px; }

  .card {
    position: absolute; left: 35px; width: 1009px; height: 520px;
    overflow: hidden;
  }
  .card--front { top: 55px; background: var(--charcoal); }
  .card--back  { top: 629px; background: var(--graphite); }

  .card__shapes { position: absolute; inset: 0; width: 100%; height: 100%; }

  .brand-arc {
    font-family: "Antonio", "Arial Narrow", sans-serif;
    font-weight: 700; fill: var(--paper);
  }

  .contact {
    position: absolute; left: 213px; top: 281px;
    font-family: "Jost", "Futura", sans-serif; font-weight: 700;
    color: var(--paper);
  }
  .contact__row { display: flex; align-items: center; height: 40px; margin-bottom: 8px; }
  .contact__icon { width: 40px; height: 40px; margin-right: 26px; flex: none; }
  .contact__phone { font-size: 24px; letter-spacing: 0.5px; }
  .contact__web { font-size: 17px; letter-spacing: 0.2px; }

  .booking {
    position: absolute; left: 305px; top: 412px;
    font-family: "Jost", "Futura", sans-serif; font-weight: 700;
    font-size: 20px; letter-spacing: 2px; color: var(--paper);
  }

  .availability {
    position: absolute; left: 640px; top: 170px; width: 330px;
    text-align: center; color: var(--ink-teal);
    font-family: "Jost", "Futura", sans-serif; font-weight: 700;
  }
  .availability__title { font-size: 60px; line-height: 1; letter-spacing: 2px; }
  .availability__hours { font-size: 52px; line-height: 1; margin-top: 30px; letter-spacing: 1px; }
  .availability__days { font-size: 21px; margin-top: 18px; letter-spacing: 1.5px; }

  .brand-wordmark {
    font-family: "Antonio", "Arial Narrow", sans-serif;
    font-weight: 700; fill: var(--teal-mist);
  }

  .footer-web {
    position: absolute; left: 480px; top: 421px;
    display: flex; align-items: center;
    font-family: "Open Sans", Arial, sans-serif; font-size: 16px;
    color: var(--paper);
  }
  .footer-web__rule { width: 90px; height: 3px; background: #d8d8d8; margin-left: 2px; }
</style>
</head>
<body>
<main class="canvas">

  <section class="card card--front">
    <svg class="card__shapes" viewBox="0 0 841 433" preserveAspectRatio="none" aria-hidden="true">
      <path fill="var(--teal-deep)" d="M346,0 L520,0 C500,60 492,150 500,230 C504,270 510,300 525,320 C480,250 470,170 440,110 C420,60 390,25 346,0 Z"/>
      <path fill="var(--teal-soft)" d="M516,0 L640,0 L640,320 L525,320 C505,280 492,200 492,130 C492,70 502,30 516,0 Z"/>
      <path fill="var(--paper)" d="M631,0 L841,0 L841,433 L611,433 C540,380 505,300 512,230 C520,130 570,50 631,0 Z"/>
      <defs>
        <path id="brandArc" d="M176,152 Q301,98 426,152"/>
      </defs>
      <text class="brand-arc" font-size="24">
        <textPath href="#brandArc" startOffset="50%" text-anchor="middle" textLength="240" lengthAdjust="spacingAndGlyphs">HIRE A VORLATRIKE BRENMOOR</textPath>
      </text>
    </svg>

    <div class="contact">
      <div class="contact__row">
        <svg class="contact__icon" viewBox="0 0 40 40" aria-hidden="true">
          <circle cx="20" cy="20" r="18" fill="none" stroke="var(--teal-soft)" stroke-width="2.5"/>
          <path fill="var(--teal-soft)" d="M14.5,12 l3,-0.5 l1.8,4.2 l-2,1.6 c0.9,2.2 2.6,3.9 4.8,4.8 l1.6,-2 l4.2,1.8 l-0.5,3 c-0.3,1 -1.2,1.6 -2.2,1.5 c-6.4,-0.6 -11.4,-5.6 -12,-12 c-0.1,-1 0.5,-1.9 1.3,-2.4 z"/>
        </svg>
        <span class="contact__phone">(555) 014-2937</span>
      </div>
      <div class="contact__row">
        <svg class="contact__icon" viewBox="0 0 40 40" aria-hidden="true">
          <circle cx="20" cy="20" r="18" fill="none" stroke="var(--teal-soft)" stroke-width="2.5"/>
          <g fill="var(--teal-soft)" stroke="var(--teal-soft)" stroke-width="1.6">
            <line x1="15" y1="20" x2="24" y2="14.5"/>
            <line x1="15" y1="20" x2="24" y2="25.5"/>
            <circle cx="15" cy="20" r="2.6"/>
            <circle cx="24.5" cy="14" r="2.6"/>
            <circle cx="24.5" cy="26" r="2.6"/>
          </g>
        </svg>
        <span class="contact__web">www.hireavorlatrikebrenmoor.example</span>
      </div>
    </div>

    <p class="booking">Réservation en ligne</p>

    <div class="availability">
      <p class="availability__title">LOCATION</p>
      <p class="availability__hours">24/24</p>
      <p class="availability__days">TOUTE LA SEMAINE</p>
    </div>
  </section>

  <section class="card card--back">
    <svg class="card__shapes" viewBox="0 0 840 432" preserveAspectRatio="none" aria-hidden="true">
      <path fill="var(--teal-steel)" d="M380,0 L620,0 C540,50 480,170 438,312 L300,400 L300,0 Z"/>
      <path fill="var(--teal-mist)" d="M300,0 L430,0 C470,70 492,150 488,200 C485,245 470,280 445,300 L300,300 Z"/>
      <path fill="var(--paper-grey)" d="M0,0 L315,0 C410,55 462,140 462,216 C462,300 410,380 320,432 L0,432 Z"/>
      <text class="brand-wordmark" x="50" y="235" font-size="64" textLength="348" lengthAdjust="spacingAndGlyphs">HIRE A VORLATRIKE BRENMOOR</text>
    </svg>

    <p class="footer-web">
      <span>www.hireavorlatrikebrenmoor.example</span>
      <span class="footer-web__rule"></span>
    </p>
  </section>

</main>
</body>
</html>
```